Business Card Upgrade

I have designed our business card using our new logo. I think it needs imporovements. We used to have two cards for our business. One card was for our software business, and the other was for our consulting business. We are now in the process of combining our websites, marketing, name, and a new logo.

Our goal is to have a really sharp professional logo. One reason I designed the card the way I did was that our Titles are sometimes long, and by separating the person's name and title, it shows up very well and the title can be adjusted no matter how long it is. Sometimes the title can be 4 or 5 words or more.

We really like our logo on black as it shows up very nice. Our PMS colors are as follows: 368C and 459C.

The Designer that will be working with us will need to deliver the following:

The front and back of the Business Card Design will need to be delivered in a high quality JPEG, and
The front and back of the Business Card Design in Illustrator Format .ai
Any fonts will need to be sent to us if they are not standard and are required to open the Illustrator file correctly.

To help us get a good idea of the card with a title, please use the title: " Director of Software Development "

NOTE: The chosen designer will be selected to design our new letterhead within 2 weeks from the closing of this contest.

To help us make sure the card design works with longer titles, please use the followign job title on the card:  

"Director of Software and Product Development"

 

ALL DESIGNERS:

1. I appreciate the different angles you are showing the cards, but please be sure and always show the direct view, so I can see the layout and what the person I hand the card will see.

2. Please do not use white.  Please use off white as I don't care for white cards and they get dirty easy and do not represent the designs well.

Dear Designers,

Please provide samples straight one as a viewer of the card will see.  Some of the angles that are presented make it impossible to tell how everything fits, and sometimes even makes areas look skewed. So, please provide a straight sample view.

Pinnacle 400 company executives such as Vice Presidents, and Directors

Software

• Professional looking Card.

Our customers are Directors, Vice Presidents, and Presidents of companies as large as Pinnacle 400 companies. The card needs to get attention wile still looking professional.

Delivery of the finished product in Illustrator Format with any fonts needed to edit the text or open the file.

The card will be a heavy stock with a soft touch coating for that silk feel.

```html
<!DOCTYPE html>
<html lang="en">
<head>
<meta charset="utf-8">
<title>Harborline Trade Group – Business Card, Front and Back</title>
<link rel="stylesheet" href="https://fonts.googleapis.com/css2?family=Arimo:wght@400&family=Montserrat:wght@800&family=Open+Sans:wght@400&display=swap">
<style>
  :root {
    --stage-light: #f1f1f1;
    --stage-dark: #c9c9c9;
    --card-black: #0a0a0a;
    --brand-green: #57ae4b;
    --brand-gold: #d8c27c;
    --logo-green: #0d6a3a;
    --label-green: #5aab4c;
    --off-white: #f7f5ee;
  }
  * { box-sizing: border-box; margin: 0; padding: 0; }
  html, body { width: 1200px; height: 720px; overflow: hidden; }
  body {
    position: relative;
    background: radial-gradient(ellipse at 50% 50%, var(--stage-light) 0%, var(--stage-dark) 100%);
    font-family: "Arimo", Arial, sans-serif;
  }
  .side-label {
    position: absolute;
    height: 72px;
    background: var(--label-green);
    color: var(--off-white);
    font-family: "Arimo", Arial, sans-serif;
    font-weight: 400;
    font-size: 48px;
    line-height: 72px;
  }
  .side-label--front { left: 0; top: 123px; width: 204px; padding-left: 8px; }
  .side-label--back { left: 994px; top: 599px; width: 206px; padding-left: 32px; }

  .card {
    position: absolute;
    width: 597px;
    height: 343px;
    background: var(--card-black);
    overflow: hidden;
  }
  .card--front { left: 307px; top: 5px; }
  .card--back { left: 309px; top: 367px; }
  .card-shapes { position: absolute; inset: 0; width: 100%; height: 100%; }
  .shape-green { fill: var(--brand-green); }
  .shape-gold { fill: var(--brand-gold); }
  .shape-black { fill: var(--card-black); }

  .brand-name {
    position: absolute;
    font-family: "Montserrat", Arial, sans-serif;
    font-weight: 800;
    color: var(--logo-green);
    text-transform: uppercase;
    line-height: 1;
    white-space: nowrap;
  }
  .card--front .brand-name { left: 56px; top: 146px; font-size: 27px; letter-spacing: 1px; }
  .card--front .brand-name span { display: block; margin-top: 10px; font-size: 16px; letter-spacing: 5.2px; }
  .card--back .brand-name { left: 6px; top: 46px; font-size: 19px; letter-spacing: 0.5px; }
  .card--back .brand-name span { display: block; margin-top: 6px; font-size: 11px; letter-spacing: 3.4px; }

  .person {
    position: absolute;
    left: 348px;
    top: 120px;
    width: 213px;
    text-align: center;
    color: var(--off-white);
  }
  .person-name {
    font-family: "Montserrat", Arial, sans-serif;
    font-weight: 800;
    font-size: 29px;
    line-height: 1;
    white-space: nowrap;
  }
  .person-title {
    margin-top: 4px;
    font-family: "Open Sans", Arial, sans-serif;
    font-size: 7px;
    text-transform: uppercase;
    white-space: nowrap;
  }
  .contact-list {
    position: absolute;
    left: 343px;
    top: 186px;
    list-style: none;
    color: var(--off-white);
    font-family: "Arimo", Arial, sans-serif;
    font-size: 15px;
  }
  .contact-item { display: flex; align-items: center; height: 23.5px; }
  .contact-icon { width: 18px; height: 18px; margin-right: 17px; fill: var(--brand-green); }
</style>
</head>
<body>
  <div class="side-label side-label--front">FRONT</div>
  <div class="side-label side-label--back">BACK</div>

  <section class="card card--front" aria-label="Business card front">
    <svg class="card-shapes" viewBox="0 0 597 343" preserveAspectRatio="none" aria-hidden="true">
      <path class="shape-gold" d="M0,0 H318 C290,100 330,225 597,322 V343 H0 Z"/>
      <path class="shape-green" d="M0,0 H291 C268,110 330,245 597,341 V343 H0 Z"/>
      <path class="shape-gold" d="M0,160 C60,260 140,320 250,343 H0 Z"/>
      <path class="shape-black" d="M0,205 C70,280 150,325 238,343 H0 Z"/>
    </svg>
    <div class="brand-name">Harborline<span>Trade Group</span></div>
  </section>

  <section class="card card--back" aria-label="Business card back">
    <svg class="card-shapes" viewBox="0 0 597 343" preserveAspectRatio="none" aria-hidden="true">
      <path class="shape-gold" d="M0,0 H214 C202,130 125,212 0,234 Z"/>
      <path class="shape-green" d="M0,0 H180 C176,112 110,192 0,222 Z"/>
    </svg>
    <div class="brand-name">Harborline<span>Trade Group</span></div>

    <div class="person">
      <p class="person-name">YOUR NAME</p>
      <p class="person-title">Director of Software and Product Development</p>
    </div>

    <ul class="contact-list">
      <li class="contact-item">
        <svg class="contact-icon" viewBox="0 0 24 24" aria-hidden="true"><path d="M6.6 10.8a15.2 15.2 0 0 0 6.6 6.6l2.2-2.2c.3-.3.7-.4 1-.2 1.1.4 2.3.6 3.6.6.6 0 1 .4 1 1V20c0 .6-.4 1-1 1A17 17 0 0 1 3 4c0-.6.4-1 1-1h3.5c.6 0 1 .4 1 1 0 1.3.2 2.5.6 3.6.1.3 0 .7-.2 1z"/></svg>
        <span>0423-223-123</span>
      </li>
      <li class="contact-item">
        <svg class="contact-icon" viewBox="0 0 24 24" aria-hidden="true"><path d="M12 2a10 10 0 1 0 0 20 10 10 0 0 0 0-20zm6.9 6h-2.9a15.6 15.6 0 0 0-1.4-3.6A8 8 0 0 1 18.9 8zM12 4c.8 1.2 1.5 2.5 1.9 4h-3.8c.4-1.5 1.1-2.8 1.9-4zM4.3 14a8.2 8.2 0 0 1 0-4h3.4a16.5 16.5 0 0 0 0 4zm.8 2h2.9c.3 1.3.8 2.5 1.4 3.6A8 8 0 0 1 5.1 16zM8 8H5.1a8 8 0 0 1 4.3-3.6C8.8 5.5 8.3 6.7 8 8zm4 12c-.8-1.2-1.5-2.5-1.9-4h3.8c-.4 1.5-1.1 2.8-1.9 4zm2.3-6H9.7a14.7 14.7 0 0 1 0-4h4.6a14.7 14.7 0 0 1 0 4zm.3 5.6c.6-1.1 1.1-2.3 1.4-3.6h2.9a8 8 0 0 1-4.3 3.6zm1.7-5.6a16.5 16.5 0 0 0 0-4h3.4a8.2 8.2 0 0 1 0 4z"/></svg>
        <span>www.website.com</span>
      </li>
      <li class="contact-item">
        <svg class="contact-icon" viewBox="0 0 24 24" aria-hidden="true"><path d="M2 5h20v14H2z M3.5 6.5 12 13l8.5-6.5" stroke="var(--card-black)" stroke-width="1.4"/></svg>
        <span>e-mail@website.com</span>
      </li>
      <li class="contact-item">
        <svg class="contact-icon" viewBox="0 0 24 24" aria-hidden="true"><path d="M12 2a7 7 0 0 0-7 7c0 5.2 7 13 7 13s7-7.8 7-13a7 7 0 0 0-7-7zm0 9.5a2.5 2.5 0 1 1 0-5 2.5 2.5 0 0 1 0 5z"/></svg>
        <span>your address will be here</span>
      </li>
    </ul>
  </section>
</body>
</html>
```